Young Accounting firm needing a captivating business card

We need a business card design that forces the person to look at the card because its either gold foil, plastic, or lettering pop up etc. We already have a logo with a specific gold color and we need to make it pop. We are an accounting firm. I need the words" accounting, payroll, licenses, audits, taxes" somewhere on the business card so as to describe what we do- preferably on the side where the logo is at.

Industry/Entity Type

Accounting

Contact Information for Business Card

Address 48276 9th Ave S Ste 305, Federal Way, WA 98117
Business Phone (360)418-2096
Fax (360)418-2157
Office Cell Phone (360)586-7319

Font styles to use
Serif

Colors
85abd2

Requirements
Must have
• It should state
• "Accounting" "Taxes" "Audits" "Licenses" "Payroll"
Nice to have
• Matte with gold foil, different textures, With Either a textured ivory background or gray blue slate background
Should not have
• colorful colors

```html
<!DOCTYPE html>
<html lang="en">
<head>
<meta charset="utf-8">
<title>Ledgerline Business Card</title>
<link rel="stylesheet" href="https://fonts.googleapis.com/css2?family=Poppins:wght@400;500;600&display=swap">
<style>
  :root {
    --backdrop: #2b2b2b;
    --gold: #b8961a;
    --gold-text: #b3911c;
    --white: #ffffff;
    --ink: #4a4a4a;
    --muted: #8c8c8c;
    --rule: #9a9a9a;
  }
  * { margin: 0; padding: 0; box-sizing: border-box; }
  html, body { width: 1200px; height: 900px; overflow: hidden; }
  body {
    background: var(--backdrop);
    font-family: "Poppins", sans-serif;
    display: flex;
    flex-direction: column;
    align-items: center;
    justify-content: center;
    gap: 36px;
  }
  .card {
    width: 720px;
    height: 411px;
    position: relative;
    box-shadow: 0 10px 30px rgba(0,0,0,0.45);
  }
  .card-front {
    background: var(--gold);
    color: var(--white);
    display: flex;
    flex-direction: column;
    align-items: center;
    justify-content: center;
  }
  .brand {
    display: flex;
    align-items: center;
    gap: 16px;
    font-size: 52px;
    font-weight: 500;
    letter-spacing: -0.5px;
    margin-top: 30px;
  }
  .brand-mark {
    width: 34px;
    height: 34px;
    background: var(--white);
  }
  .services {
    position: absolute;
    bottom: 44px;
    left: 0;
    right: 0;
    text-align: center;
    font-size: 17px;
    letter-spacing: 0.3px;
  }
  .services .dot { margin: 0 6px; font-size: 12px; vertical-align: middle; }

  .card-back {
    background: var(--white);
  }
  .identity {
    position: absolute;
    right: 420px;
    top: 150px;
    text-align: right;
  }
  .person-name {
    color: var(--gold-text);
    font-size: 32px;
    font-weight: 500;
    line-height: 1.1;
  }
  .person-title {
    color: var(--muted);
    font-size: 18px;
    font-weight: 400;
  }
  .divider {
    position: absolute;
    left: 318px;
    top: 130px;
    width: 1px;
    height: 138px;
    background: var(--rule);
  }
  .contact-list {
    position: absolute;
    left: 340px;
    top: 126px;
    list-style: none;
    color: var(--ink);
    font-size: 20px;
    line-height: 28px;
  }
  .contact-list li, .address {
    display: flex;
    align-items: center;
    gap: 10px;
  }
  .icon { width: 18px; height: 18px; fill: var(--gold-text); flex: none; }
  .address {
    position: absolute;
    left: 170px;
    bottom: 70px;
    color: var(--ink);
    font-size: 20px;
  }
  .address .icon { width: 20px; height: 24px; }
</style>
</head>
<body>

<section class="card card-front">
  <div class="brand"><span class="brand-mark"></span>Ledgerline</div>
  <p class="services">Accounting<span class="dot">•</span>Taxes<span class="dot">•</span>Audits<span class="dot">•</span>Licenses<span class="dot">•</span>Payroll</p>
</section>

<section class="card card-back">
  <div class="identity">
    <h1 class="person-name">Daniel Morrow</h1>
    <p class="person-title">Founder &amp; CEO</p>
  </div>
  <div class="divider"></div>
  <ul class="contact-list">
    <li><svg class="icon" viewBox="0 0 24 24"><path d="M6.6 10.8a15.1 15.1 0 0 0 6.6 6.6l2.2-2.2a1 1 0 0 1 1-.25 11.4 11.4 0 0 0 3.6.57 1 1 0 0 1 1 1V20a1 1 0 0 1-1 1A17 17 0 0 1 3 4a1 1 0 0 1 1-1h3.5a1 1 0 0 1 1 1c0 1.25.2 2.45.57 3.57a1 1 0 0 1-.25 1z"/></svg>(360)418-2096</li>
    <li><svg class="icon" viewBox="0 0 24 24"><path d="M7 2h10a1.5 1.5 0 0 1 1.5 1.5v17A1.5 1.5 0 0 1 17 22H7a1.5 1.5 0 0 1-1.5-1.5v-17A1.5 1.5 0 0 1 7 2zm.5 2v14h9V4zm4.5 15.2a1 1 0 1 0 0 2 1 1 0 0 0 0-2z"/></svg>(360)586-7319</li>
    <li><svg class="icon" viewBox="0 0 24 24"><path d="M7 2h8l3 3v5H7zM3 11h18a1 1 0 0 1 1 1v7a1 1 0 0 1-1 1H3a1 1 0 0 1-1-1v-7a1 1 0 0 1 1-1zm2 3v2h6v-2z"/></svg>(360)418-2157</li>
    <li><svg class="icon" viewBox="0 0 24 24"><path d="M2 5h20v14H2zm2 2v.4l8 5.2 8-5.2V7zm0 2.8V17h16V9.8l-8 5.2z"/></svg>info@ledgerlinetax.com</li>
    <li><svg class="icon" viewBox="0 0 24 24"><path d="M12 2a10 10 0 1 0 0 20 10 10 0 0 0 0-20zm-1 17.9A8 8 0 0 1 4.2 10.2L9 15v1a2 2 0 0 0 2 2zm6.9-2.5A2 2 0 0 0 16 16h-1v-3a1 1 0 0 0-1-1H8v-2h2a1 1 0 0 0 1-1V7h2a2 2 0 0 0 2-2v-.4a8 8 0 0 1 2.9 12.8z"/></svg>www.ledgerlinetax.com</li>
  </ul>
  <p class="address"><svg class="icon" viewBox="0 0 20 24"><path d="M10 0a8 8 0 0 0-8 8c0 6 8 16 8 16s8-10 8-16a8 8 0 0 0-8-8zm0 11a3 3 0 1 1 0-6 3 3 0 0 1 0 6z"/></svg>48276 9th Ave S Ste 305, Federal Way, WA 98117</p>
</section>

</body>
</html>
```